Website for SaaS CRM software

We require a cool website for a new SaaS CRM software. The design needs to be slick and modern. I quite like the look of sites like PostBadger.

The character 'Rhonda' in the video is the main character which we would like to incorporate on each page if possible. Like the chimp on Postbadger website.

'Sign Up Free' button or form to feature throughout the site so we have a strong call to action.

Here is a short video which will give you an idea of the software:
https://clipvault.example/83920417
Password: plintx

You can login to the user software (backend) for screen grabs and to see what the software is all about:
www.taskorbitq.example
Username: tenant8
Password: tenant8

Please note: The website is for the front end which is where we sell the software and NOT once the user has logged in.

Target Market(s)

Small businesses, freelancers, designers, 1-man businesses

Industry/Entity Type

Software

Requirements
Must have
• 1. Opt-in box for getting started for free:

'Sign up for your Free account'

2. Logos for social media : Qp/Chirpel/ViewDeck/JobLoop / K+
3. Friendora 'LIKE' button
4.The Navigation Bar should always be on display at the top when scrolling
5. Login button near the Navigation Bar
6. Login page or pop-up should also have 'Forgot Password' link which prompts them to enter their email so a password can be emailed to them.

5 pages & a blog in total. The pages we require are:

HOME
- Heading 'Easy to use small business software'
- Should have a video placeholder and some bullet points or tick marks for key features. The video (from ViewDeck) should open up on a bigger lightbox and the background greyed out.
- Sign up box to have the fields for First Name, Company Name, Email & Password with a check box for 'I agree with Terms & Conditions'

TOUR
Sub-Navigation bar at the top or side bar with the headings for each module i.e CONTACTS, QUOTES, JOBS, DIARY, SALES, PURCHASES, PRODUCTS, REPORTS
Each module with need to have a placeholder for an image or video and 1 paragraph of text explaining key features. Please see http://postbadger.example/features/

See how the Navigation buttons stay visible at all times and changes to the next button when scrolling: http://postbadger.example/features/

No side bar on this page.

PRICING
Pricing table of 3 to 4 columns with a button at the bottom. This software is a monthly subscription, so we need to show the $/month for each Plan at the top with the name of the Plan
The plans are:
Bronze: Free
Silver: $20/month
Gold: $40 / month
Platinum: $75 / month

No side bar on this page.

Heading at the bottom: 'No minimum contract. Cancel anytime.'

SUPPORT PAGE
This to a contact form to submit a ticket for tech support. We also need a 2-column list for videos which we will put up. The video open up on a lightbox in bigger size.

No side bar on this page.

CONTACT
Contact details i.e name, address, telephone, email & a contact form
No side bar on this page.

BLOG
Pagemill blog. I love the way the headings, paragraph, font, line spacing, colours are on the PostBadger blog.

Need a side bar.

```html
<!DOCTYPE html>
<html lang="en">
<head>
<meta charset="utf-8">
<title>TaskOrbit – Easy to Use Small Business Software</title>
<link rel="stylesheet" href="https://fonts.googleapis.com/css2?family=Montserrat:wght@400;500;600;700;800&display=swap">
<style>
  :root {
    --header-top: #fbfbfb;
    --header-bottom: #eeeeee;
    --ink: #111111;
    --nav-text: #555555;
    --nav-line: #dddddd;
    --brand-blue: #2a93dd;
    --brand-blue-dark: #1874c4;
    --accent-blue: #46c4ec;
    --hero-blue: #48c3ea;
    --screen-fill: #fffccd;
    --screen-frame: #0b0b0b;
    --silver-top: #d9d9d9;
    --silver-bottom: #a9a9a9;
    --card-white: #ffffff;
    --card-border: #d9e3e8;
    --heading-blue: #2795dd;
    --body-text: #222222;
    --footer-bg: #333333;
    --footer-text: #ffffff;
    --social-a: #2c6fb7;
    --social-b: #4fb8e8;
    --social-c: #1d7bb3;
    --social-d: #e02b27;
    --social-e: #4a4a4a;
  }
  * { box-sizing: border-box; margin: 0; padding: 0; }
  html, body { width: 1200px; height: 830px; overflow: hidden; }
  body { font-family: "Montserrat", Arial, sans-serif; background: var(--hero-blue); position: relative; }

  /* Header */
  .site-header {
    position: absolute; left: 0; top: 0; width: 1200px; height: 148px;
    background: linear-gradient(var(--header-top), var(--header-bottom));
    box-shadow: 0 2px 6px rgba(0,0,0,.25);
    z-index: 2;
  }
  .brand {
    position: absolute; left: 70px; top: 50px;
    display: flex; align-items: center; gap: 12px;
    font-size: 50px; font-weight: 800; color: var(--ink); letter-spacing: -1px;
  }
  .brand-dot { width: 22px; height: 22px; border-radius: 50%; background: var(--brand-blue); }
  .btn-signup {
    position: absolute; left: 420px; top: 53px; width: 177px; height: 50px;
    border-radius: 6px; background: linear-gradient(#45a9ec, var(--brand-blue-dark));
    box-shadow: 0 2px 0 #155c9c;
    color: #fff; font-weight: 700; font-size: 22px;
    display: flex; align-items: center; justify-content: center;
  }
  .main-nav {
    position: absolute; left: 607px; top: 53px; width: 523px; height: 50px;
    background: #fff; border-radius: 6px; box-shadow: 0 2px 3px rgba(0,0,0,.18);
    display: flex; list-style: none; overflow: hidden;
  }
  .main-nav li {
    flex: auto; display: flex; align-items: center; justify-content: center;
    font-size: 18px; color: var(--nav-text); border-right: 1px solid var(--nav-line);
  }
  .main-nav li:last-child { border-right: none; }
  .like-button {
    position: absolute; left: 957px; top: 18px;
    display: flex; align-items: center; gap: 4px; font-size: 11px; color: #3b5998;
  }
  .like-button .like-label { border: 1px solid #9aa9c8; background: #eceef5; padding: 3px 6px; border-radius: 3px; }
  .like-button .like-count { border: 1px solid #bbb; background: #fff; color: #333; padding: 3px 5px; border-radius: 3px; }
  .login-link { position: absolute; left: 1055px; top: 18px; font-size: 19px; font-weight: 700; color: var(--ink); }

  /* Hero */
  .hero {
    position: absolute; left: 0; top: 148px; width: 1200px; height: 598px;
    background:
      radial-gradient(ellipse 160px 90px at 255px 20px, rgba(255,255,255,.55), transparent),
      linear-gradient(135deg, transparent 40%, rgba(255,255,255,.12) 40%, rgba(255,255,255,.12) 62%, transparent 62%),
      var(--hero-blue);
  }
  .video-monitor { position: absolute; left: 97px; top: 68px; width: 583px; }
  .monitor-screen { height: 344px; background: var(--screen-frame); padding: 18px; border-radius: 3px 3px 0 0; }
  .video-still { width: 100%; height: 100%; background: linear-gradient(90deg, #fffbc5, var(--screen-fill)); }
  .monitor-chin { height: 53px; background: linear-gradient(var(--silver-top), var(--silver-bottom)); border-radius: 0 0 3px 3px; }
  .monitor-stand {
    width: 170px; height: 70px; margin: 0 auto;
    background: linear-gradient(#c9c9c9, #f4f4f4);
    clip-path: polygon(18% 0, 82% 0, 100% 100%, 0 100%);
    border-radius: 0 0 12px 12px;
  }
  .monitor-shadow {
    width: 520px; height: 24px; margin: -8px auto 0; border-radius: 50%;
    background: radial-gradient(rgba(0,0,0,.22), transparent 70%);
  }

  .features-card {
    position: absolute; left: 716px; top: 68px; width: 398px; height: 397px;
    background: var(--card-white); border: 2px solid var(--card-border); border-radius: 4px;
    box-shadow: 0 0 0 3px rgba(255,255,255,.5), inset 0 0 12px rgba(0,0,0,.06);
    padding: 28px 24px 0 30px;
  }
  .features-title { color: var(--heading-blue); font-size: 32px; font-weight: 700; line-height: 33px; margin-bottom: 28px; }
  .feature-list { list-style: none; }
  .feature-list li {
    position: relative; padding-left: 22px; font-size: 15px; line-height: 20px;
    color: var(--body-text); margin-bottom: 19px;
  }
  .feature-list li::before {
    content: ""; position: absolute; left: 2px; top: 5px;
    border-left: 6px solid var(--heading-blue); border-top: 5px solid transparent; border-bottom: 5px solid transparent;
  }

  .cta-pill {
    position: absolute; left: 611px; top: 500px; width: 499px; height: 54px;
    background: #050505; border-radius: 27px; box-shadow: 0 10px 14px -6px rgba(0,0,0,.35);
    color: #fff; font-size: 27px; font-weight: 700;
    display: flex; align-items: center; justify-content: center; gap: 8px;
  }
  .cta-pill .cta-highlight { color: var(--accent-blue); }

  /* Footer */
  .site-footer {
    position: absolute; left: 0; top: 746px; width: 1200px; height: 84px; background: var(--footer-bg);
  }
  .copyright { position: absolute; left: 92px; top: 34px; color: var(--footer-text); font-size: 15px; font-weight: 500; }
  .social-links { position: absolute; left: 866px; top: 19px; display: flex; gap: 5px; list-style: none; }
  .social-links li {
    width: 48px; height: 48px; border-radius: 50%;
    display: flex; align-items: center; justify-content: center;
    color: #fff; font-size: 9px; font-weight: 600;
  }
  .social-qp { background: var(--social-a); }
  .social-chirpel { background: var(--social-b); }
  .social-jobloop { background: var(--social-c); }
  .social-viewdeck { background: var(--social-d); }
  .social-kplus { background: var(--social-e); }
</style>
</head>
<body>
  <header class="site-header">
    <div class="brand"><span>TaskOrbit</span><span class="brand-dot"></span></div>
    <a class="btn-signup">Sign Up Free</a>
    <ul class="main-nav">
      <li>Home</li><li>Tour</li><li>Pricing</li><li>Support</li><li>Comtact</li><li>Blog</li>
    </ul>
    <div class="like-button"><span class="like-label">Like</span><span class="like-count">3.6k</span></div>
    <a class="login-link">Log In</a>
  </header>

  <main class="hero">
    <div class="video-monitor">
      <div class="monitor-screen">
        <div class="video-still" role="img" aria-label="Product introduction video placeholder"></div>
      </div>
      <div class="monitor-chin"></div>
      <div class="monitor-stand"></div>
      <div class="monitor-shadow"></div>
    </div>

    <section class="features-card">
      <h1 class="features-title">Easy to Use Small Business Software</h1>
      <ul class="feature-list">
        <li>Quisque eget lorem mi, sed lacinia quam.</li>
        <li>Ut quis felis diam, id sodales velit.</li>
        <li>Curabitur dapibus ligula nec mi aliquam fermentum.</li>
        <li>Fusce in nulla eleifend orci molestie pellentesque eget consequat tellus.</li>
        <li>Etiam non odio est, ut molestie mauris.</li>
      </ul>
    </section>

    <a class="cta-pill">Sign Up For <span class="cta-highlight">Your Free Account</span></a>
  </main>

  <footer class="site-footer">
    <p class="copyright">© 2012 TaskOrbit, All rights reserved.</p>
    <ul class="social-links">
      <li class="social-qp">Qp</li>
      <li class="social-chirpel">Chirpel</li>
      <li class="social-jobloop">JobLoop</li>
      <li class="social-viewdeck">ViewDeck</li>
      <li class="social-kplus">K+</li>
    </ul>
  </footer>
</body>
</html>
```